Military and tactical gear supply company needs web design

We need a web design for a company called U.S. Ravenfield. We provide quality tactical equipment to military and law enforcement. This is an e-commerce business and we primarily market ourselves on social media. Our key products are backpacks, military-style belts, and tactical flashlights. The gear we sell is not yet widely known about, but is on par with the state-of-the-art products in this field. We want the website to convey the message of quality, durability, and reliability. We use the word "kinetic" because the customers in this field are very "action-oriented" and we would like that idea to be communicated in the web site as well. The primary demographic is men in their 20's-30's, so the web site should have a masculine feel to it. Attached is the logo and color scheme.

```html
<!DOCTYPE html>
<html lang="en">
<head>
<meta charset="utf-8">
<title>U.S. Ravenfield — Tactical Equipment</title>
<link rel="stylesheet" href="https://fonts.googleapis.com/css2?family=Montserrat:wght@400;500;600;700&family=Roboto:wght@400;500;700&display=swap">
<style>
:root{
  --ink:#231f20;
  --red:#c1272d;
  --steel:#2c5f7c;
  --page:#f5f5f5;
  --line:#e4e4e4;
  --text:#333;
  --muted:#8a8a8a;
  --link:#2c6a8f;
}
*{box-sizing:border-box;margin:0;padding:0}
html,body{width:781px;height:1200px;overflow:hidden}
body{position:relative;background:var(--page);font-family:Roboto,Arial,sans-serif;color:var(--text)}
.abs{position:absolute}
.topbar{left:0;top:0;width:781px;height:17px;background:var(--ink);color:#fff;font-size:6.5px;font-weight:500}
.topbar .tagline{left:105px;top:5px}
.topbar .links{right:105px;top:0;display:flex;height:17px;align-items:center;gap:17px}
.topbar .signin{background:var(--steel);height:17px;padding:0 7px;display:flex;align-items:center}
.header{left:0;top:17px;width:781px;height:49px;background:#fff;border-bottom:1px solid var(--line)}
.brand{left:105px;top:13px;font-family:Montserrat,sans-serif;font-weight:700;font-size:17px;color:var(--ink);letter-spacing:.3px;line-height:1}
.brand small{display:block;font-size:6.5px;font-weight:500;text-align:right;margin-top:2px;letter-spacing:.2px}
.nav{right:105px;top:18px;display:flex;align-items:center;font-family:Montserrat,sans-serif;font-size:7px;font-weight:700;color:var(--ink)}
.nav a{padding:3px 3px;margin-left:14px;color:inherit;text-decoration:none}
.nav a.active{background:var(--red);color:#fff;margin-left:0}
.nav .sep{width:1px;height:12px;background:#ddd;margin-left:10px}
.nav svg{margin-left:10px}
.hero{left:25px;top:78px;width:731px;height:244px;overflow:hidden;
  background:
    radial-gradient(ellipse 110px 70px at 290px 200px,rgba(150,125,85,.75),rgba(150,125,85,0) 70%),
    radial-gradient(ellipse 140px 120px at 110px 80px,rgba(120,120,112,.9),rgba(120,120,112,0) 75%),
    radial-gradient(ellipse 200px 60px at 300px 130px,rgba(25,24,24,.85),rgba(25,24,24,0) 75%),
    radial-gradient(ellipse 120px 110px at 60px 200px,rgba(95,92,84,.9),rgba(95,92,84,0) 80%),
    linear-gradient(100deg,#77746d 0%,#5a5852 28%,#3a3634 50%,#262223 65%,#231f20 100%)}
.hero .arrow{top:110px}
.promo{left:446px;top:107px;width:230px;height:184px;border:2px solid #fff;color:#fff;font-family:Montserrat,sans-serif;padding:20px 17px}
.promo .kicker{font-size:11.5px;font-weight:400}
.promo .title{font-size:14px;font-weight:700;margin-top:1px}
.promo .rule{width:34px;height:3px;background:var(--red);margin:9px 0 12px}
.promo .big{font-size:43px;font-weight:700;line-height:1;letter-spacing:.5px}
.promo .btn{display:inline-block;margin-top:15px;border:1.5px solid #fff;font-size:8.5px;font-weight:600;padding:5px 12px}
h2{font-family:Montserrat,sans-serif;font-weight:700;font-size:17px;color:var(--ink);text-align:center;width:781px;left:0;letter-spacing:.3px}
.cards{left:105px;top:398px;width:571px;height:196px;display:flex;background:#fff;border:1px solid var(--line)}
.card{flex:1;border-left:1px solid var(--line);text-align:center;padding-top:18px}
.card:first-child{border-left:0}
.card .ph{width:100px;height:100px;margin:0 auto}
.card .name{font-family:Montserrat,sans-serif;font-size:9px;font-weight:500;margin-top:18px;color:var(--ink)}
.card .shop{display:inline-block;margin-top:13px;font-family:Montserrat,sans-serif;font-size:6.5px;font-weight:700;letter-spacing:.6px;color:var(--red);border:1px solid var(--red);padding:4px 6px}
.card .shop.solid{background:var(--red);color:#fff}
.band{left:105px;top:628px;width:571px;height:87px;
  background:
    radial-gradient(ellipse 120px 40px at 380px 30px,rgba(90,92,78,.6),rgba(90,92,78,0)),
    radial-gradient(ellipse 140px 40px at 200px 70px,rgba(80,80,70,.55),rgba(80,80,70,0)),
    linear-gradient(90deg,#2a2625,#3d3b36 50%,#2a2625)}
.band .head{left:19px;top:23px;color:#fff;font-family:Montserrat,sans-serif;font-weight:700;font-size:16px;line-height:22px}
.band .btn{right:19px;top:33px;border:1.5px solid #fff;color:#fff;font-family:Montserrat,sans-serif;font-weight:700;font-size:7.5px;letter-spacing:.8px;padding:6px 12px}
.recs{left:105px;top:791px;width:571px;display:flex;justify-content:space-between}
.rec{width:83px;text-align:center}
.rec .tile{height:87px;background:#fff;border:1px solid var(--line);display:flex;align-items:center;justify-content:center}
.rec .ph{width:70px;height:70px}
.rec .lbl{font-size:7px;color:var(--link);margin-top:9px}
.values{left:0;top:924px;width:781px;height:76px;background:#fff;display:flex;align-items:center;padding:0 105px}
.value{flex:1;display:flex;align-items:center;justify-content:center;gap:8px;font-family:Montserrat,sans-serif;font-weight:500;font-size:10.5px;color:var(--ink);border-left:1px solid var(--line);height:30px}
.value:first-child{border-left:0;justify-content:flex-start}
.value:last-child{justify-content:flex-end}
.footer{left:0;top:1000px;width:781px;height:200px;background:var(--ink);color:var(--muted);font-size:7px}
.col{top:36px;width:140px}
.col h4{font-family:Montserrat,sans-serif;font-size:8.5px;font-weight:700;color:#fff;margin-bottom:8px;letter-spacing:.2px}
.col li{list-style:none;line-height:13.7px;display:flex;align-items:center;gap:4px}
.col.dim li{color:#5f5a58}
.col li.hot{color:var(--red)}
.dot{width:5px;height:5px;background:var(--muted)}
.col p{line-height:10px;margin-top:-1px}
.field{margin-top:17px;width:132px;height:20px;border:1px solid #777;display:flex;align-items:center;padding-left:6px;gap:5px;font-size:6.5px}
.submit{display:inline-block;margin-top:10px;background:var(--red);color:#fff;font-weight:700;font-size:6.5px;padding:5px 8px}
.legal{left:105px;top:170px;width:571px;border-top:1px solid #444;padding-top:11px;display:flex;justify-content:space-between;font-size:6.5px}
.legal nav span{margin-right:16px}
.legal .red{color:var(--red)}
</style>
</head>
<body>

<div class="abs topbar">
  <span class="abs tagline">LOREM IPSUM DOLOR SIT AMET, CONSECTETUR</span>
  <div class="abs links"><span>ABOUT US</span><span>LOCATION</span><span>+123 456 7890</span><span class="signin">SIGN IN</span></div>
</div>

<header class="abs header">
  <div class="abs brand">U.S. RAVENFIELD<small>usravenfield.com</small></div>
  <nav class="abs nav">
    <a class="active">HOME</a><a>PRODUCTS</a><a>HISTORY</a><a>LE/NSN/MIL</a><a>CONTACT</a>
    <span class="sep"></span>
    <svg width="10" height="10" viewBox="0 0 10 10"><circle cx="4" cy="4" r="3" fill="none" stroke="#231f20" stroke-width="1.6"/><line x1="6.2" y1="6.2" x2="9.2" y2="9.2" stroke="#231f20" stroke-width="1.8"/></svg>
    <span class="sep"></span>
    <svg width="12" height="14" viewBox="0 0 12 14"><circle cx="9" cy="3" r="3" fill="#c1272d"/><path d="M0 4h2l1.5 6h6l1.5-4.5H3" fill="#231f20"/><circle cx="4" cy="12" r="1.2" fill="#231f20"/><circle cx="9" cy="12" r="1.2" fill="#231f20"/></svg>
  </nav>
</header>

<section class="abs hero" role="img" aria-label="Soldier in helmet aiming a rifle with optic sight, gloved hand on the grip">
  <svg class="abs arrow" style="left:26px" width="10" height="20" viewBox="0 0 10 20"><path d="M8 2 2 10l6 8" fill="none" stroke="#fff" stroke-width="1.5"/></svg>
  <svg class="abs arrow" style="right:26px" width="10" height="20" viewBox="0 0 10 20"><path d="M2 2l6 8-6 8" fill="none" stroke="#777" stroke-width="1.5"/></svg>
</section>
<div class="abs promo">
  <div class="kicker">U.S. RAVENFIELD’S</div>
  <div class="title">EXCLUSIVE COLLECTION</div>
  <div class="rule"></div>
  <div class="big">15% OFF</div>
  <div class="btn">SHOP NOW</div>
</div>

<h2 class="abs" style="top:352px">FEATURED PRODUCTS</h2>
<div class="abs cards">
  <div class="card"><div class="ph" role="img" aria-label="Camouflage tactical backpack" style="background:radial-gradient(ellipse 32px 48px at 50% 50%,#a8977a 0%,#c2b08a 55%,rgba(194,176,138,0) 100%)"></div><div class="name">BACKPACKS</div><span class="shop solid">SHOP NOW</span></div>
  <div class="card"><div class="ph" role="img" aria-label="Camouflage military belt with buckle" style="background:radial-gradient(ellipse 52px 34px at 50% 48%,#b8a57a 0%,#9a8d66 50%,rgba(154,141,102,0) 100%)"></div><div class="name">MILITARY STYLE BELTS</div><span class="shop">SHOP NOW</span></div>
  <div class="card"><div class="ph" role="img" aria-label="Two black tactical flashlights" style="background:radial-gradient(ellipse 50px 26px at 50% 50%,#2a2a2a 0%,#3c3c3c 55%,rgba(60,60,60,0) 100%)"></div><div class="name">TACTICAL FLASHLIGHTS</div><span class="shop">SHOP NOW</span></div>
  <div class="card"><div class="ph" role="img" aria-label="Camouflage combat shirt" style="background:radial-gradient(ellipse 34px 50px at 50% 50%,#5f5e52 0%,#8c8a7a 55%,rgba(140,138,122,0) 100%)"></div><div class="name">GEAR</div><span class="shop">SHOP NOW</span></div>
</div>

<section class="abs band" role="img" aria-label="Rows of uniformed soldiers in muted tones">
  <div class="abs head">QUALITY TACTICAL MILITARY<br>&amp; LAW ENFORCEMENT EQUIPMENT</div>
  <div class="abs btn">BROWSE MORE PRODUCTS</div>
</section>

<h2 class="abs" style="top:745px">RECOMMENDED FOR YOU</h2>
<div class="abs recs">
  <div class="rec"><div class="tile"><div class="ph" role="img" aria-label="Tactical vest pack" style="background:radial-gradient(ellipse 26px 32px at 50% 50%,#7d6a45 0%,#a08a5c 55%,rgba(160,138,92,0) 100%)"></div></div><div class="lbl">Backpacks</div></div>
  <div class="rec"><div class="tile"><div class="ph" role="img" aria-label="Tactical flashlight with lanyard" style="background:radial-gradient(ellipse 18px 34px at 55% 50%,#1a1a1a 0%,#333 55%,rgba(51,51,51,0) 100%)"></div></div><div class="lbl">Tactical Flashlight</div></div>
  <div class="rec"><div class="tile"><div class="ph" role="img" aria-label="Olive military belt" style="background:radial-gradient(ellipse 36px 14px at 50% 50%,#6a6c4a 0%,#7b7d5a 60%,rgba(123,125,90,0) 100%)"></div></div><div class="lbl">Military Style Belts</div></div>
  <div class="rec"><div class="tile"><div class="ph" role="img" aria-label="Camouflage field cap" style="background:radial-gradient(ellipse 34px 20px at 50% 55%,#9a8f70 0%,#b3a886 55%,rgba(179,168,134,0) 100%)"></div></div><div class="lbl">Military Gear</div></div>
  <div class="rec"><div class="tile"><div class="ph" role="img" aria-label="Camouflage backpack" style="background:radial-gradient(ellipse 26px 34px at 50% 50%,#a0906a 0%,#b9a982 55%,rgba(185,169,130,0) 100%)"></div></div><div class="lbl">Backpacks</div></div>
  <div class="rec"><div class="tile"><div class="ph" role="img" aria-label="Compact tactical flashlight" style="background:radial-gradient(ellipse 36px 16px at 50% 50%,#111 0%,#3a3a3a 55%,rgba(58,58,58,0) 100%)"></div></div><div class="lbl">Tactical Flashlight</div></div>
</div>

<section class="abs values">
  <div class="value"><svg width="22" height="26" viewBox="0 0 22 26" fill="none" stroke="#2c5f7c" stroke-width="1.3"><circle cx="11" cy="10" r="8"/><path d="M11 5l1.5 3h3l-2.4 2 1 3.2-3.1-1.8-3.1 1.8 1-3.2L6.5 8h3z"/><path d="M6 16l-2 8 3-2 2 3 2-6M16 16l2 8-3-2-2 3-2-6"/></svg>Quality Products</div>
  <div class="value"><svg width="22" height="24" viewBox="0 0 22 24" fill="none" stroke="#2c5f7c" stroke-width="1.4"><path d="M11 1l9 3v7c0 6-4 10-9 12C6 21 2 17 2 11V4z"/><circle cx="11" cy="12" r="5"/><path d="M8.5 12l2 2 3.5-4"/></svg>Durability</div>
  <div class="value"><svg width="26" height="24" viewBox="0 0 26 24" fill="none" stroke="#2c5f7c" stroke-width="1.3"><rect x="6" y="2" width="14" height="10" rx="1"/><line x1="6" y1="5" x2="20" y2="5"/><path d="M2 10l5 5h5l3 3M24 12l-5 5h-3M2 16l6 6M24 18l-4 4"/></svg>Reliable Services</div>
</section>

<footer class="abs footer">
  <div class="abs col dim" style="left:105px"><h4>CONTACT US</h4><ul><li>Contact Us</li><li>Order Status</li><li>Downloadable Forms</li><li>Shipping Information</li><li>Returns &amp; Exchanges</li><li class="hot">Gift Cards</li></ul></div>
  <div class="abs col" style="left:251px"><h4>QUICK LINKS</h4><ul><li>About Us</li><li>Blog</li><li>Terms and conditions</li><li>Help Center</li></ul></div>
  <div class="abs col" style="left:398px"><h4>STAY CONNECTED</h4><ul><li><span class="dot"></span>Friendbook</li><li><span class="dot"></span>Chirper</li><li><span class="dot"></span>Snapframe</li><li><span class="dot"></span>ViewTube</li><li><span class="dot"></span>ProLink</li></ul></div>
  <div class="abs col" style="left:544px"><h4>SUBSCRIBE US</h4><p>Subscribe our newsletter to get latest news and updates about tutorials.</p>
    <div class="field"><svg width="8" height="6" viewBox="0 0 8 6" fill="none" stroke="#8a8a8a" stroke-width=".8"><rect x=".5" y=".5" width="7" height="5"/><path d="M.5 .5l3.5 3 3.5-3"/></svg>Your email Address</div>
    <span class="submit">SUBMIT</span></div>
  <div class="abs legal">
    <nav><span class="red">Home</span><span>Products</span><span>History</span><span>LE/NSN/MIL</span><span>Contact</span></nav>
    <div>© 2020 <span class="red">US Ravenfield.com</span> All rights reserved. | Design By Northgate Webworks Ltd.</div>
  </div>
</footer>

</body>
</html>
```